Design 2015 Winter themed holiday card

We need a holiday card for our company.

The attached brief provides all the information for the design. We provided two images for the cover or if you have something better.

CARD DESIGN 4" x 6" Vertical Folded Card
Bleed: The extra .0625" on each side of your artwork that bleeds off the edge of the piece and ensures your piece will not end up with white borders.
Trim: The final size the printed piece will be.
Safe: The .0625" area from the final trim size. Do not place text or important imagery beyond the safe line to avoid it getting cut off when the finished piece is trimmed to final size.
Corner Rounding, where available, can be 1/8" or 5/16". Examples are provided in the image below.
1/8" is a "tighter" or "smaller" corner radius.
5/16" is a "wider" or "larger" corner radius.

Target Market(s)

Government agencies, businesses and nonprofits

Industry/Entity Type

It Company

Font styles to use
Serif
Sans Serif

Requirements
Must have
• Please follow the design brief: QKRP-Strategy-Brief-Holiday-Card-11042015.pdf
• It includes the fonts, colors, design parameters - please review it before designing. I've included two previous holiday cards for your review.
• Please add "Seasons Greetings" on the cover.

```html
<!DOCTYPE html>
<html lang="en">
<head>
<meta charset="utf-8">
<title>Holiday Card – Inside Spread</title>
<link rel="stylesheet" href="https://fonts.googleapis.com/css2?family=Arimo:ital@0;1&family=Allura&family=Dancing+Script:wght@700&family=Great+Vibes&family=Mr+Dafoe&family=Parisienne&family=Herr+Von+Muellerhoff&display=swap">
<style>
  :root {
    --paper: #ffffff;
    --ink: #111111;
    --signature-ink: #1a1a1a;
  }
  html, body {
    margin: 0;
    padding: 0;
    overflow: hidden;
    background: var(--paper);
  }
  .card-spread {
    position: relative;
    width: 1200px;
    height: 900px;
    background: var(--paper);
    overflow: hidden;
  }
  .signature-panel, .message-panel {
    position: absolute;
    top: 0;
    width: 600px;
    height: 900px;
  }
  .signature-panel { left: 0; }
  .message-panel { left: 600px; }

  .signature {
    position: absolute;
    margin: 0;
    white-space: nowrap;
    color: var(--signature-ink);
    line-height: 1;
    transform-origin: left center;
  }
  .sig-nora   { left: 312px; top: 226px; font: 34px "Allura", cursive; transform: rotate(5deg); }
  .sig-greta  { left: 100px; top: 280px; font: 30px "Parisienne", cursive; transform: rotate(-5deg); }
  .sig-marco  { left: 275px; top: 332px; font: 700 32px "Dancing Script", cursive; }
  .sig-ivan   { left: 116px; top: 398px; font: 30px "Great Vibes", cursive; transform: rotate(-12deg); }
  .sig-delia  { left: 364px; top: 430px; font: 28px "Mr Dafoe", cursive; transform: rotate(7deg); }
  .sig-lena   { left: 216px; top: 484px; font: 27px "Parisienne", cursive; }
  .sig-owen   { left: 346px; top: 560px; font: 38px "Herr Von Muellerhoff", cursive; transform: rotate(10deg); }
  .sig-simone { left: 108px; top: 578px; font: 700 28px "Dancing Script", cursive; transform: rotate(-3deg); }

  .message {
    position: absolute;
    left: 0;
    width: 600px;
    top: 298px;
    text-align: center;
    color: var(--ink);
    font-family: "Arimo", Arial, sans-serif;
    font-size: 19px;
    line-height: 38px;
  }
  .message p { margin: 0; }
  .greeting {
    margin-top: 34px !important;
  }
  .sender {
    font-style: italic;
  }
</style>
</head>
<body>
  <main class="card-spread">
    <section class="signature-panel" aria-label="Team signatures">
      <p class="signature sig-nora">Nora Bellamy</p>
      <p class="signature sig-greta">Greta Pollard</p>
      <p class="signature sig-marco">Marco Tellman</p>
      <p class="signature sig-ivan">Ivan Roake</p>
      <p class="signature sig-delia">Delia Frost</p>
      <p class="signature sig-lena">Lena Vandorp</p>
      <p class="signature sig-simone">Simone Kettler</p>
      <p class="signature sig-owen">Owen Castell</p>
    </section>
    <section class="message-panel">
      <div class="message">
        <p>As this year draws to a close, we are grateful<br>
        for the opportunities we have had to work together.<br>
        We wish you all the best for the year to come.</p>
        <p class="greeting">Happy Holidays</p>
        <p class="sender">from the Clear Current Writing team</p>
      </div>
    </section>
  </main>
</body>
</html>
```